New Website Announcement

We need a flyer to announce our new website to customers and prospective clients. The website will be launching soon, but I can provide a detailed outline in PDF form with copy and imagery to serve as inspiration for this design.

I would like a postcard size document that can be mailed in an envelope (no need for postcard style mailer info on 1 side)

About my company:

Clarity Through Craft is a new breed of marketing consulting agency built for the next frontier of consumer learning. Social interaction will be at the heart of great insights going forward – in how consumers engage with brands and in how organizations socialize what they learn to gain competitive advantage.
By fusing innovative insights techniques, technology and compelling graphic design-based reporting, we ensure results get noticed and make an impact.

contact info that can also be included:

Email: dana@clarity-through-craft.example

Phone: 607-352-8814

New High Res logo file has been added. (.ai)

Thanks

Attention all designers submitting a design for this project. Please keep in mind a few important details about this project.

1. Remember that the main objective of this postcard is to announce my new website.

2. Please be sure to read the brief for the copy I would like on each side. You can be creative in how it is displayed, but I need this key information somewhere. All other copy on the attached files is for your background only.

3. Please do not submit overly simple designs that just take the images I provided and overlay a text box with my copy. I could easily do this myself in PowerPoint in 5 minutes.

4. Remember that the design should be edgy and modern but needs to be professional and speak to a business audience.

Please submit any questions. Thank you for your submissions. 

Dana

Illustrator high res logo file now correctly uploaded. Thanks.

Target Market(s)

senior level marketing and research clients at large companies and agencies

Industry/Entity Type

Marketing

Requirements
Must have
• Main message:

Need an engaging way to tell customers and prospective clients that we have a new website and that they should come visit us online to learn more about out services, check out case studies and read about our exciting partnerships.

COPY TO USE - UPDATED

Side 1:
(logo)
Introducing Clarity Through Craft

Let’s talk about taking research out of the dark ages.

Visit our newly launched website to learn how and get in touch.

www.clarity-through-craft.example

Side 2
Logo
followed by tagline:
Consumer insights that get noticed.
A leading-edge marketing partnership that really works.

Additional text to use on Side 2:
How we can help...

Think of us as your go-to resource for identifying and incorporating the most innovative and exciting techniques into your research programs. We carefully curate and develop close partnerships with the best of the best - from online qualitative research and mobile ethnography to social media listening and fresh takes on concept testing, we can guide the way.

Plus, we believe that socializing consumer learning is just as critical as gathering it.By taking insights deliverables to the next level – through infographics, videos, magazines,interactive profiles and so much more – we are getting stakeholders excited to engage with research and inspired to take action because of it.
It’s a new way to look at insights from a new type of partner. And, it’s a new way to get the most from your research dollars.
Nice to have
• could incorporate our website main image of the lamp on white brick background which is attached, but not 100% mandatory.
Should not have
• - should not be too playful or young, but needs to be modern and design focused

- should not be cluttered or overly 'salesy'

- needs to be upscale and elegant / compelling and aligned with the look and feel of the website imagery (see attached)

```html
<!DOCTYPE html>
<html lang="en">
<head>
<meta charset="utf-8">
<title>Clarity Through Craft – New Website Postcard</title>
<link rel="stylesheet" href="https://fonts.googleapis.com/css2?family=Arimo:ital,wght@0,700;1,700&family=Tinos:ital,wght@1,700&family=Didact+Gothic&family=Open+Sans:wght@700&family=Jost:ital,wght@1,700&display=swap">
<style>
  :root {
    --stage: #2b2b2b;
    --ink: #1c1c1c;
    --blue: #1a73c9;
    --blue-deep: #0f4f9c;
    --paper: #ffffff;
    --brick-light: #e4e4e4;
    --brick-mid: #b9b9b9;
    --brick-dark: #8e8e8e;
    --floor: #c9c9c9;
    --band: #0b0b0b;
  }
  * { box-sizing: border-box; margin: 0; padding: 0; }
  html, body {
    width: 881px; height: 1200px; overflow: hidden;
    background: var(--stage);
  }
  .postcard {
    position: absolute; overflow: hidden;
    box-shadow: 0 6px 18px rgba(0,0,0,.55);
  }
  .postcard--front { left: 100px; top: 70px; width: 678px; height: 470px; }
  .postcard--back  { left: 104px; top: 625px; width: 672px; height: 460px; }

  .photo { position: absolute; inset: 0; }
  .postcard--front .photo {
    background:
      radial-gradient(ellipse 260px 200px at 190px 90px, rgba(255,255,255,.75), rgba(255,255,255,0) 70%),
      linear-gradient(180deg, var(--brick-light) 0%, var(--brick-mid) 62%, var(--brick-dark) 70%, var(--floor) 74%, #dcdcdc 100%);
  }
  .postcard--back .photo {
    top: 40px;
    background: linear-gradient(180deg, #d9d9d9 0%, #f2f2f2 45%, #bdbdbd 66%, #d6d6d6 72%, #ededed 100%);
  }

  .wordmark {
    position: absolute;
    font-family: "Arimo", Arial, sans-serif; font-weight: 700;
    color: var(--blue); text-transform: uppercase;
    line-height: 1.04; letter-spacing: 1px; white-space: nowrap;
  }
  .postcard--front .wordmark { left: 105px; top: 176px; font-size: 34px; }
  .postcard--back .wordmark { left: 426px; top: 342px; font-size: 32px; }

  .intro-box {
    position: absolute; left: 387px; top: 142px; width: 283px; height: 153px;
    border-radius: 12px; border: 2px solid #fff;
    background: linear-gradient(180deg, #ffffff 0%, #e6e6e6 55%, #bdbdbd 100%);
    box-shadow: 0 2px 8px rgba(0,0,0,.35);
    text-align: center; font-family: "Arimo", Arial, sans-serif; font-style: italic; font-weight: 700;
    padding-top: 16px;
  }
  .intro-box__kicker { color: var(--blue); font-size: 26px; }
  .intro-box__name { color: var(--ink); font-size: 23px; margin-top: 6px; }
  .intro-box__line { color: var(--ink); font-size: 15px; line-height: 1.3; margin-top: 12px; }

  .visit {
    position: absolute; right: 8px; top: 375px; text-align: right;
    font-family: "Tinos", "Times New Roman", serif; font-style: italic; font-weight: 700;
    font-size: 20px; line-height: 1.3; color: var(--ink);
  }
  .visit__lead { color: var(--blue); }

  .url-band {
    position: absolute; left: 0; right: 0; top: 440px; height: 30px; background: var(--band);
  }
  .url-band__slash {
    position: absolute; left: 185px; top: 8px; width: 52px; height: 22px;
    background: var(--blue); transform: skewX(-40deg);
  }
  .url-band__text {
    position: absolute; right: 8px; top: 3px;
    font-family: "Arimo", Arial, sans-serif; font-style: italic; font-weight: 700;
    font-size: 17px; letter-spacing: 4.5px; color: var(--blue); white-space: nowrap;
  }

  .top-strip { position: absolute; left: 0; right: 0; top: 0; height: 40px; background: var(--band); }
  .blue-band {
    position: absolute; left: 420px; right: 0; top: 48px; height: 24px;
    background: linear-gradient(180deg, var(--blue) 0%, var(--blue-deep) 100%);
  }

  .help-panel {
    position: absolute; left: 30px; top: 12px; width: 388px; height: 318px;
    background: linear-gradient(135deg, #ffffff 0%, #f4f4f4 60%, #d8d8d8 100%);
    border-radius: 4px; box-shadow: 0 3px 10px rgba(0,0,0,.4);
    padding: 10px 11px;
  }
  .help-panel__tagline {
    font-family: "Jost", "Futura", sans-serif; font-style: italic; font-weight: 700;
    color: var(--blue); font-size: 13.5px; line-height: 1.35; white-space: nowrap;
    padding-bottom: 6px; border-bottom: 1px solid #bbb;
  }
  .help-panel__title {
    font-family: "Open Sans", Arial, sans-serif; font-weight: 700;
    font-size: 20px; color: var(--ink); margin-top: 4px;
  }
  .help-panel__body {
    font-family: "Didact Gothic", "Century Gothic", sans-serif;
    font-size: 11px; line-height: 1.3; color: #2a2a2a; margin-top: 2px;
  }
  .help-panel__body + .help-panel__body { margin-top: 10px; }

  .url-ribbon {
    position: absolute; left: 0; top: 393px; width: 330px; height: 34px;
    background: var(--blue-deep);
    clip-path: polygon(0 0, 100% 0, 94% 50%, 100% 100%, 0 100%);
    font-family: "Arimo", Arial, sans-serif; font-style: italic; font-weight: 700;
    font-size: 16px; color: var(--paper); padding: 7px 0 0 10px; white-space: nowrap;
  }
</style>
</head>
<body>

<section class="postcard postcard--front">
  <div class="photo" role="img" aria-label="Arched floor lamp lighting a white brick wall above a concrete floor"></div>
  <div class="wordmark">Clarity<br>Through<br>Craft</div>
  <div class="intro-box">
    <p class="intro-box__kicker">Introducing</p>
    <p class="intro-box__name">Clarity Through Craft</p>
    <p class="intro-box__line">Let’s talk about taking research<br>out of the dark ages.</p>
  </div>
  <p class="visit"><span class="visit__lead">VISIT OUR</span> newly launched website<br>to learn how and get in touch.</p>
  <div class="url-band">
    <span class="url-band__slash"></span>
    <span class="url-band__text">www.clarity-through-craft.example</span>
  </div>
</section>

<section class="postcard postcard--back">
  <div class="top-strip"></div>
  <div class="photo" role="img" aria-label="White painted brick wall above a pale concrete floor"></div>
  <div class="blue-band"></div>
  <article class="help-panel">
    <p class="help-panel__tagline">Consumer insights that get noticed.<br>A leading-edge marketing partnership that really works.</p>
    <h2 class="help-panel__title">How we can help...</h2>
    <p class="help-panel__body">Think of us as your go-to resource for identifying and incorporating the most innovative and exciting techniques into your research programs. We carefully curate and develop close partnerships with the best of the best - from online qualitative research and mobile ethnography to social media listening and fresh takes on concept testing, we can guide the way.</p>
    <p class="help-panel__body">Plus, we believe that socializing consumer learning is just as critical as gathering it. By taking insights deliverables to the next level – through infographics, videos, magazines, interactive profiles and so much more – we are getting stakeholders excited to engage with research and inspired to take action because of it. It’s a new way to look at insights from a new type of partner. And, it’s a new way to get the most from your research dollars.</p>
  </article>
  <div class="url-ribbon">www.clarity-through-craft.example</div>
  <div class="wordmark">Clarity<br>Through<br>Craft</div>
</section>

</body>
</html>
```